Kelmora Legal Business Card

I require a corporate business card for a new legal services business.

I do not have a logo, nor do I want one.

I require a clean, neat a professional card for a law firm.

Details:

Business Name: Kelmora Legal
Name: Debra Lindqvist
Title: Corporate Services Manager
Location: Office 14 (Top Floor), Toravel Business Centre, Quinlan Grove Street, Alotau CBD, Milne Bay Province.
Postal Address: PO Box 593, Alotau, 211, Milne Bay Province, Papua New Guinea.
Contact: T: +675 6418250, F: +675 6413362, M: +675 72915867, E: dlindqvist@kelmoraexample.com.pg.

I look forward to your design submissions.

Industry/Entity Type

Legal

```html
<!DOCTYPE html>
<html lang="en">
<head>
<meta charset="utf-8">
<title>Kelmora Legal – Business Card Colourways</title>
<link href="https://fonts.googleapis.com/css2?family=Cinzel:wght@600&family=Federo&family=Arimo:wght@400&display=swap" rel="stylesheet">
<style>
  :root {
    --board: #1c1f18;
    --paper: #f4f4f4;
    --ink: #222222;
    --contact: #ffffff;
    --rule: #9a9a9a;
  }
  * { box-sizing: border-box; margin: 0; padding: 0; }
  html, body { width: 1200px; height: 900px; overflow: hidden; background: var(--board); }
  .board { position: relative; width: 1200px; height: 900px; background: radial-gradient(ellipse at center, #262a20 0%, var(--board) 75%); }

  .card {
    position: absolute; width: 578px; height: 356px; overflow: hidden;
    box-shadow: 0 0 22px 6px rgba(255,255,240,.45);
    font-family: "Arimo", Arial, sans-serif;
  }
  .card--purple { left: 20px;  top: 65px;  --accent: #a61fc2; --accent-dark: #7d1296; --band: #3df08c; --band-light: #8af7b8; --brand: #8e2c9e; }
  .card--orange { left: 612px; top: 65px;  --accent: #e2801a; --accent-dark: #9a5210; --band: #2f45ec; --band-light: #5f7bf7; --brand: #c3661c; }
  .card--red    { left: 20px;  top: 498px; --accent: #e01c1c; --accent-dark: #9c0f0f; --band: #4ba8ef; --band-light: #8cc9f7; --brand: #b31a1a; }
  .card--green  { left: 612px; top: 498px; --accent: #1cc25a; --accent-dark: #0f8a3c; --band: #f0415e; --band-light: #f7889c; --brand: #1aa64a; }

  .card__top { position: absolute; left: 0; top: 0; width: 100%; height: 20px;
    background: linear-gradient(90deg, var(--accent-dark), var(--accent) 50%, var(--accent-dark)); }
  .card__header { position: absolute; left: 0; top: 20px; width: 100%; height: 132px;
    background: linear-gradient(100deg, #f7f7f7 0%, #e6e4e2 45%, #f4f4f4 100%); }
  .card__band { position: absolute; left: 0; top: 152px; width: 100%; height: 164px;
    background: linear-gradient(90deg, var(--band) 0%, var(--band) 55%, var(--band-light) 100%); }
  .card__bottom { position: absolute; left: 0; bottom: 0; width: 100%; height: 40px;
    background: linear-gradient(90deg, var(--accent-dark), var(--accent) 50%, var(--accent-dark)); }
  .card__notch { position: absolute; left: 426px; top: 152px; width: 0; height: 0;
    border-left: 9px solid transparent; border-right: 9px solid transparent; border-top: 10px solid #f2f2f2; }

  .brand__mark { position: absolute; left: 98px; top: 26px; width: 74px; height: 58px; border-radius: 50%; background: var(--accent); }
  .brand__name { position: absolute; left: 30px; top: 96px; width: 220px; text-align: center;
    font-family: "Cinzel", Georgia, serif; font-weight: 600; font-size: 31px; color: var(--brand); letter-spacing: .5px; white-space: nowrap; }

  .person { position: absolute; left: 300px; top: 52px; width: 264px; text-align: center; }
  .person__name { font-family: "Federo", "Trebuchet MS", sans-serif; font-size: 28px; color: var(--brand); line-height: 34px; white-space: nowrap; }
  .person__rule { width: 200px; height: 1px; background: var(--rule); margin: 2px auto 4px; }
  .person__title { font-size: 19px; line-height: 23px; color: var(--ink); }

  .contact { position: absolute; left: 56px; top: 162px; list-style: none; color: var(--contact); font-size: 14.5px; }
  .contact__item { position: absolute; left: 0; display: flex; align-items: flex-start; gap: 9px; white-space: nowrap; line-height: 20px; }
  .contact__item--address { top: 0; }
  .contact__item--postal  { top: 56px; }
  .contact__item--phone   { top: 94px; }
  .contact__item--email   { top: 127px; }
  .contact__icon { flex: none; width: 15px; height: 15px; margin-top: 3px; border-radius: 3px; background: var(--accent); display: block; }
  .contact__label { color: var(--accent-dark); }
</style>
</head>
<body>
<main class="board">

  <!-- Purple colourway -->
  <article class="card card--purple">
    <div class="card__top"></div>
    <div class="card__header" role="img" aria-label="Soft faded background photo of a judge's gavel"></div>
    <div class="card__band"></div>
    <div class="card__bottom"></div>
    <div class="card__notch"></div>
    <span class="brand__mark"></span>
    <div class="brand__name">Kelmora Legal</div>
    <div class="person">
      <div class="person__name">Debra Lindqvist</div>
      <div class="person__rule"></div>
      <div class="person__title">Corporate Services<br>Manager</div>
    </div>
    <ul class="contact">
      <li class="contact__item contact__item--address">
        <svg class="contact__icon" viewBox="0 0 16 16"><path d="M8 3a3 3 0 0 0-3 3c0 2.2 3 6 3 6s3-3.8 3-6a3 3 0 0 0-3-3z" fill="#fff"/><circle cx="8" cy="6" r="1.1" fill="currentColor"/></svg>
        <span>Office 14 (Top Floor), Toravel Business Centre,<br>Quinlan Grove Street, Alotau CBD, Milne Bay Province.</span>
      </li>
      <li class="contact__item contact__item--postal">
        <svg class="contact__icon" viewBox="0 0 16 16"><rect x="4" y="5" width="8" height="7" fill="none" stroke="#fff" stroke-width="1.3"/><line x1="4" y1="8" x2="12" y2="8" stroke="#fff" stroke-width="1.1"/></svg>
        <span>PO Box 593, Alotau, 211, Milne Bay Province,Papua New Guinea.</span>
      </li>
      <li class="contact__item contact__item--phone">
        <svg class="contact__icon" viewBox="0 0 16 16"><path d="M4 6c0-1 .8-1.6 1.6-1.6h4.8C11.2 4.4 12 5 12 6v.8H9.6V6H6.4v.8H4z" fill="#fff"/><rect x="4.6" y="8" width="6.8" height="4" rx="1" fill="#fff"/></svg>
        <span><span class="contact__label">T:</span> +675 6418250, <span class="contact__label">F:</span> +675 6413362, <span class="contact__label">M:</span> +675 72915867</span>
      </li>
      <li class="contact__item contact__item--email">
        <svg class="contact__icon" viewBox="0 0 16 16"><rect x="3.5" y="5" width="9" height="6.5" fill="#fff"/><path d="M3.5 5 8 8.6 12.5 5" fill="none" stroke="#999" stroke-width="1"/></svg>
        <span>dlindqvist@kelmoraexample.com.pg.</span>
      </li>
    </ul>
  </article>

  <!-- Orange colourway -->
  <article class="card card--orange">
    <div class="card__top"></div>
    <div class="card__header" role="img" aria-label="Soft faded background photo of a judge's gavel"></div>
    <div class="card__band"></div>
    <div class="card__bottom"></div>
    <div class="card__notch"></div>
    <span class="brand__mark"></span>
    <div class="brand__name">Kelmora Legal</div>
    <div class="person">
      <div class="person__name">Debra Lindqvist</div>
      <div class="person__rule"></div>
      <div class="person__title">Corporate Services<br>Manager</div>
    </div>
    <ul class="contact">
      <li class="contact__item contact__item--address">
        <svg class="contact__icon" viewBox="0 0 16 16"><path d="M8 3a3 3 0 0 0-3 3c0 2.2 3 6 3 6s3-3.8 3-6a3 3 0 0 0-3-3z" fill="#fff"/><circle cx="8" cy="6" r="1.1" fill="currentColor"/></svg>
        <span>Office 14 (Top Floor), Toravel Business Centre,<br>Quinlan Grove Street, Alotau CBD, Milne Bay Province.</span>
      </li>
      <li class="contact__item contact__item--postal">
        <svg class="contact__icon" viewBox="0 0 16 16"><rect x="4" y="5" width="8" height="7" fill="none" stroke="#fff" stroke-width="1.3"/><line x1="4" y1="8" x2="12" y2="8" stroke="#fff" stroke-width="1.1"/></svg>
        <span>PO Box 593, Alotau, 211, Milne Bay Province,Papua New Guinea.</span>
      </li>
      <li class="contact__item contact__item--phone">
        <svg class="contact__icon" viewBox="0 0 16 16"><path d="M4 6c0-1 .8-1.6 1.6-1.6h4.8C11.2 4.4 12 5 12 6v.8H9.6V6H6.4v.8H4z" fill="#fff"/><rect x="4.6" y="8" width="6.8" height="4" rx="1" fill="#fff"/></svg>
        <span><span class="contact__label">T:</span> +675 6418250, <span class="contact__label">F:</span> +675 6413362, <span class="contact__label">M:</span> +675 72915867</span>
      </li>
      <li class="contact__item contact__item--email">
        <svg class="contact__icon" viewBox="0 0 16 16"><rect x="3.5" y="5" width="9" height="6.5" fill="#fff"/><path d="M3.5 5 8 8.6 12.5 5" fill="none" stroke="#999" stroke-width="1"/></svg>
        <span>dlindqvist@kelmoraexample.com.pg.</span>
      </li>
    </ul>
  </article>

  <!-- Red colourway -->
  <article class="card card--red">
    <div class="card__top"></div>
    <div class="card__header" role="img" aria-label="Soft faded background photo of a judge's gavel"></div>
    <div class="card__band"></div>
    <div class="card__bottom"></div>
    <div class="card__notch"></div>
    <span class="brand__mark"></span>
    <div class="brand__name">Kelmora Legal</div>
    <div class="person">
      <div class="person__name">Debra Lindqvist</div>
      <div class="person__rule"></div>
      <div class="person__title">Corporate Services<br>Manager</div>
    </div>
    <ul class="contact">
      <li class="contact__item contact__item--address">
        <svg class="contact__icon" viewBox="0 0 16 16"><path d="M8 3a3 3 0 0 0-3 3c0 2.2 3 6 3 6s3-3.8 3-6a3 3 0 0 0-3-3z" fill="#fff"/><circle cx="8" cy="6" r="1.1" fill="currentColor"/></svg>
        <span>Office 14 (Top Floor), Toravel Business Centre,<br>Quinlan Grove Street, Alotau CBD, Milne Bay Province.</span>
      </li>
      <li class="contact__item contact__item--postal">
        <svg class="contact__icon" viewBox="0 0 16 16"><rect x="4" y="5" width="8" height="7" fill="none" stroke="#fff" stroke-width="1.3"/><line x1="4" y1="8" x2="12" y2="8" stroke="#fff" stroke-width="1.1"/></svg>
        <span>PO Box 593, Alotau, 211, Milne Bay Province,Papua New Guinea.</span>
      </li>
      <li class="contact__item contact__item--phone">
        <svg class="contact__icon" viewBox="0 0 16 16"><path d="M4 6c0-1 .8-1.6 1.6-1.6h4.8C11.2 4.4 12 5 12 6v.8H9.6V6H6.4v.8H4z" fill="#fff"/><rect x="4.6" y="8" width="6.8" height="4" rx="1" fill="#fff"/></svg>
        <span><span class="contact__label">T:</span> +675 6418250, <span class="contact__label">F:</span> +675 6413362, <span class="contact__label">M:</span> +675 72915867</span>
      </li>
      <li class="contact__item contact__item--email">
        <svg class="contact__icon" viewBox="0 0 16 16"><rect x="3.5" y="5" width="9" height="6.5" fill="#fff"/><path d="M3.5 5 8 8.6 12.5 5" fill="none" stroke="#999" stroke-width="1"/></svg>
        <span>dlindqvist@kelmoraexample.com.pg.</span>
      </li>
    </ul>
  </article>

  <!-- Green colourway -->
  <article class="card card--green">
    <div class="card__top"></div>
    <div class="card__header" role="img" aria-label="Soft faded background photo of a judge's gavel"></div>
    <div class="card__band"></div>
    <div class="card__bottom"></div>
    <div class="card__notch"></div>
    <span class="brand__mark"></span>
    <div class="brand__name">Kelmora Legal</div>
    <div class="person">
      <div class="person__name">Debra Lindqvist</div>
      <div class="person__rule"></div>
      <div class="person__title">Corporate Services<br>Manager</div>
    </div>
    <ul class="contact">
      <li class="contact__item contact__item--address">
        <svg class="contact__icon" viewBox="0 0 16 16"><path d="M8 3a3 3 0 0 0-3 3c0 2.2 3 6 3 6s3-3.8 3-6a3 3 0 0 0-3-3z" fill="#fff"/><circle cx="8" cy="6" r="1.1" fill="currentColor"/></svg>
        <span>Office 14 (Top Floor), Toravel Business Centre,<br>Quinlan Grove Street, Alotau CBD, Milne Bay Province.</span>
      </li>
      <li class="contact__item contact__item--postal">
        <svg class="contact__icon" viewBox="0 0 16 16"><rect x="4" y="5" width="8" height="7" fill="none" stroke="#fff" stroke-width="1.3"/><line x1="4" y1="8" x2="12" y2="8" stroke="#fff" stroke-width="1.1"/></svg>
        <span>PO Box 593, Alotau, 211, Milne Bay Province,Papua New Guinea.</span>
      </li>
      <li class="contact__item contact__item--phone">
        <svg class="contact__icon" viewBox="0 0 16 16"><path d="M4 6c0-1 .8-1.6 1.6-1.6h4.8C11.2 4.4 12 5 12 6v.8H9.6V6H6.4v.8H4z" fill="#fff"/><rect x="4.6" y="8" width="6.8" height="4" rx="1" fill="#fff"/></svg>
        <span><span class="contact__label">T:</span> +675 6418250, <span class="contact__label">F:</span> +675 6413362, <span class="contact__label">M:</span> +675 72915867</span>
      </li>
      <li class="contact__item contact__item--email">
        <svg class="contact__icon" viewBox="0 0 16 16"><rect x="3.5" y="5" width="9" height="6.5" fill="#fff"/><path d="M3.5 5 8 8.6 12.5 5" fill="none" stroke="#999" stroke-width="1"/></svg>
        <span>dlindqvist@kelmoraexample.com.pg.</span>
      </li>
    </ul>
  </article>

</main>
</body>
</html>
```